Modern Business Card for Industrial Company

We need business cards updated with modern fonts and make it look more technical, sharp and clean. The logo should not be changed, but we are looking for fresh solutions for how other information on the card is laid out in an interesting way. The company provides machinery and services to the ceramic industry and deals with cutting-edge technology. The design should reflect a technologically advanced and modern company that deals with the latest European technologies.

Font styles to use
Sans Serif

Requirements
Must have
• Modern fonts, technical look and feel

```html
<!DOCTYPE html>
<html lang="en">
<head>
<meta charset="utf-8">
<title>Kelva Service – Business Card</title>
<link href="https://fonts.googleapis.com/css2?family=Open+Sans:ital,wght@0,400;0,700;1,400;1,700&display=swap" rel="stylesheet">
<style>
  :root {
    --page-bg: #2a2a2c;
    --card-bg: #141414;
    --brand-blue: #0f5fa8;
    --accent-red: #c8202a;
    --text-light: #c9cbce;
    --text-muted: #9a9ca0;
  }
  * { margin: 0; padding: 0; box-sizing: border-box; }
  html, body {
    width: 1200px; height: 900px; overflow: hidden;
    background: var(--page-bg);
    font-family: "Open Sans", Arial, sans-serif;
  }
  .sheet {
    width: 1200px; height: 900px;
    display: flex; flex-direction: column;
    align-items: center; justify-content: center; gap: 40px;
  }
  .card {
    width: 640px; height: 366px;
    background: var(--card-bg);
    box-shadow: 0 10px 30px rgba(0,0,0,.45);
    position: relative;
  }
  .brand-mark {
    display: flex; align-items: center; gap: 12px;
    color: var(--brand-blue);
    font-weight: 700;
    text-transform: uppercase;
    letter-spacing: 3px;
    line-height: 1;
  }
  .brand-mark__square {
    width: 14px; height: 14px; background: var(--accent-red); flex: none;
  }
  .card--front .brand-mark {
    position: absolute; left: 44px; top: 156px; font-size: 30px;
  }
  .card--front .divider {
    position: absolute; left: 336px; top: 92px;
    width: 1px; height: 182px; background: var(--brand-blue);
  }
  .contact {
    position: absolute; left: 366px; top: 104px;
    color: var(--text-light);
    font-size: 14px; line-height: 1.45;
  }
  .contact__name {
    color: var(--brand-blue); font-weight: 700; font-style: italic;
    text-transform: uppercase; font-size: 18px; letter-spacing: .5px;
  }
  .contact__role { color: var(--text-muted); font-size: 14px; margin-bottom: 10px; }
  .contact__address { margin-bottom: 8px; }
  .contact__line { display: flex; align-items: center; gap: 8px; }
  .contact__line svg { width: 12px; height: 12px; flex: none; fill: var(--accent-red); }
  .card--back { display: flex; align-items: center; justify-content: center; }
  .card--back .brand-mark { font-size: 42px; }
  .card--back .brand-mark__square { width: 18px; height: 18px; }
</style>
</head>
<body>
<main class="sheet">
  <section class="card card--front" aria-label="Business card front">
    <div class="brand-mark"><span class="brand-mark__square"></span>Kelva Service</div>
    <div class="divider"></div>
    <div class="contact">
      <p class="contact__name">Marco Ferretti</p>
      <p class="contact__role">President</p>
      <p class="contact__address">418 Kiln Parkway, Suite 200<br>Dunmore, GA 30120</p>
      <p class="contact__line">
        <svg viewBox="0 0 24 24" aria-hidden="true"><path d="M6.6 10.8a15.1 15.1 0 0 0 6.6 6.6l2.2-2.2c.3-.3.7-.4 1-.2 1.1.4 2.3.6 3.6.6.6 0 1 .4 1 1V20c0 .6-.4 1-1 1A17 17 0 0 1 3 4c0-.6.4-1 1-1h3.5c.6 0 1 .4 1 1 0 1.3.2 2.5.6 3.6.1.3 0 .7-.2 1z"/></svg>
        (404) 555.0187
      </p>
      <p class="contact__line">
        <svg viewBox="0 0 24 24" aria-hidden="true"><path d="M2 5h20v14H2z M2 5l10 8 10-8" stroke="#141414" stroke-width="1.5"/></svg>
        mferretti@kelvaservice.com
      </p>
      <p class="contact__line">
        <svg viewBox="0 0 24 24" aria-hidden="true"><circle cx="12" cy="12" r="10"/><path d="M2 12h20M12 2c3 3 3 17 0 20M12 2c-3 3-3 17 0 20" stroke="#141414" stroke-width="1.5" fill="none"/></svg>
        www.kelvaservice.com
      </p>
    </div>
  </section>
  <section class="card card--back" aria-label="Business card back">
    <div class="brand-mark"><span class="brand-mark__square"></span>Kelva Service</div>
  </section>
</main>
</body>
</html>
```